Professional & attention grabbing.

A business card design, front and back. I already have a logo I will attach, but I am open to something new as well.
Things to include:
Name:
Title:
Phone:
Email:
Wanting something that is professional but attention grabbing.
Also we do a lot of work using drones on natural gas pipelines (WATCHING THE LINE)if you want to include any of that. I'm open to ideas.
Target Market(s)
Natural gas transmission industry / greenhouse gas mitigation industry
Industry/Entity Type
Business
Contact Information for Business Card
All details have been conveyed above.
Colors
Designer to choose colors to be used in the design.
Look and feel
Each slider illustrates characteristics of the customer's brand and the style your logo design should communicate.

```html
<!DOCTYPE html>
<html lang="en">
<head>
<meta charset="utf-8">
<title>Halvick Inspections – Business Card</title>
<link href="https://fonts.googleapis.com/css2?family=Red+Hat+Display:wght@700&family=Roboto:wght@400;500&display=swap" rel="stylesheet">
<style>
  :root {
    --stage: #000000;
    --paper: #ffffff;
    --brand-red: #c8202e;
    --ink-dark: #3a3b3c;
    --ink-muted: #636363;
  }
  * { box-sizing: border-box; margin: 0; padding: 0; }
  html, body {
    width: 976px; height: 1200px; overflow: hidden;
    background: var(--stage);
    font-family: "Roboto", Arial, sans-serif;
  }
  .canvas { position: relative; width: 976px; height: 1200px; }

  .card {
    position: absolute; left: 148px; width: 680px; height: 389px;
    background: var(--paper); overflow: hidden;
  }
  .card--front { top: 126px; }
  .card--back { top: 665px; }

  .band { position: absolute; background: var(--brand-red); }
  .card--front .band { top: 137px; width: 27px; height: 128px; }
  .card--front .band--left { left: 0; }
  .card--front .band--right { right: 0; }
  .card--back .band { top: 182px; height: 49px; }
  .card--back .band--left { left: 0; width: 159px; }
  .card--back .band--right { right: 0; width: 163px; }

  .brand {
    position: absolute; display: flex; align-items: center; gap: 14px;
    color: var(--ink-dark);
  }
  .brand__mark { width: 70px; height: 70px; background: var(--ink-dark); flex: none; }
  .brand__name {
    font-family: "Roboto", Arial, sans-serif; font-weight: 500;
    font-size: 34px; line-height: 1.05; letter-spacing: 0.5px;
  }
  .card--front .brand { left: 78px; top: 159px; width: 290px; height: 102px; }
  .card--back .brand { left: 199px; top: 156px; width: 290px; height: 100px; }

  .tagline {
    position: absolute; left: 196px; top: 268px; width: 288px;
    text-align: center; font-size: 18px; letter-spacing: 5.6px;
    color: var(--ink-dark); white-space: nowrap;
  }

  .person { position: absolute; left: 401px; top: 76px; }
  .person__name {
    font-family: "Red Hat Display", "Roboto", sans-serif; font-weight: 700;
    font-size: 30px; color: var(--brand-red); letter-spacing: -0.5px; line-height: 1.1;
  }
  .person__title { font-size: 25px; color: var(--ink-muted); line-height: 1.2; margin-top: 1px; }

  .contact { position: absolute; left: 396px; top: 176px; list-style: none; }
  .contact__item {
    display: flex; align-items: center; gap: 8px;
    height: 24px; margin-bottom: 7.5px;
    font-size: 16px; color: var(--ink-muted); letter-spacing: 0.2px;
  }
  .contact__icon { width: 23px; height: 23px; flex: none; }
</style>
</head>
<body>
<div class="canvas">

  <section class="card card--front" aria-label="Card front">
    <div class="band band--left"></div>
    <div class="band band--right"></div>

    <div class="brand">
      <span class="brand__mark"></span>
      <span class="brand__name">Halvick<br>Inspections</span>
    </div>

    <div class="person">
      <p class="person__name">Daniel Marsh</p>
      <p class="person__title">Title</p>
    </div>

    <ul class="contact">
      <li class="contact__item">
        <svg class="contact__icon" viewBox="0 0 24 24" fill="none" stroke="#c8202e" stroke-width="1.4">
          <circle cx="12" cy="12" r="11"/><rect x="8.5" y="5.5" width="7" height="13" rx="1.2"/><line x1="11" y1="16.5" x2="13" y2="16.5"/>
        </svg>
        <span>&nbsp;555-014-2290</span>
      </li>
      <li class="contact__item">
        <svg class="contact__icon" viewBox="0 0 24 24" fill="none" stroke="#c8202e" stroke-width="1.4">
          <circle cx="12" cy="12" r="11"/><rect x="6" y="8" width="12" height="8"/><polyline points="6,8 12,13 18,8"/>
        </svg>
        <span>name@example.com</span>
      </li>
      <li class="contact__item">
        <svg class="contact__icon" viewBox="0 0 24 24">
          <circle cx="12" cy="12" r="11" fill="none" stroke="#c8202e" stroke-width="1.4"/>
          <path d="M12 5.5a4.5 4.5 0 0 0-4.5 4.5c0 3.4 4.5 8.5 4.5 8.5s4.5-5.1 4.5-8.5A4.5 4.5 0 0 0 12 5.5z" fill="#c8202e"/>
          <circle cx="12" cy="10" r="1.7" fill="#fff"/>
        </svg>
        <span>your street address here</span>
      </li>
      <li class="contact__item">
        <svg class="contact__icon" viewBox="0 0 24 24" fill="none" stroke="#c8202e" stroke-width="1.2">
          <circle cx="12" cy="12" r="11" stroke-width="1.4"/><circle cx="12" cy="12" r="6"/>
          <ellipse cx="12" cy="12" rx="2.6" ry="6"/><line x1="6" y1="12" x2="18" y2="12"/>
        </svg>
        <span>www.your website name</span>
      </li>
    </ul>
  </section>

  <section class="card card--back" aria-label="Card back">
    <div class="band band--left"></div>
    <div class="band band--right"></div>

    <div class="brand">
      <span class="brand__mark"></span>
      <span class="brand__name">Halvick<br>Inspections</span>
    </div>

    <p class="tagline">WATCHING THE LINE</p>
  </section>

</div>
</body>
</html>
```